Professional, Scientific Cover Design for Nutritional / Hair Tissue Mineral Analysis (HTMA) Company

Hair tissue mineral analysis is a versatile, science-backed tool that offers a deeper understanding of your body's mineral and heavy metal profile. By evaluating long-term mineral balance and toxic exposures, HTMA provides invaluable insights that can aid in optimizing nutrition, addressing chronic health issues, and creating a personalized wellness strategy.

We have updated our logo and are in need of an updated report cover in which personalized test results are placed. We are looking for a professional and more modern look.

There are 2 small cutouts that will need to remain as shown in the picture in the brief.

Our updated logo along with color palette used will be uploaded in the brief as well as our 2 previous, outdated designs. We no longer want our address on the front cover. We also do not want images with people in them.

Thank you.

Website: www.pevdosk.com

Designs look the same

• Images with people

```html
<!DOCTYPE html>
<html lang="en">
<head>
<meta charset="utf-8">
<title>Hair Tissue Mineral Analysis – Report Cover</title>
<link href="https://fonts.googleapis.com/css2?family=Lexend+Exa:wght@700&display=swap" rel="stylesheet">
<style>
  :root {
    --sky-white: #f7fafd;
    --mist-blue: #c9dcec;
    --mid-blue: #5a8cc0;
    --deep-blue: #1d4f8e;
    --navy: #123a73;
    --title-blue: #2c55a3;
    --cutout: #ffffff;
    --cutout-edge: #d6e2ee;
    --mark-text: #ffffff;
  }
  html, body {
    margin: 0;
    padding: 0;
    width: 945px;
    height: 1200px;
    overflow: hidden;
  }
  .cover {
    position: relative;
    width: 945px;
    height: 1200px;
    overflow: hidden;
    background:
      radial-gradient(ellipse 70% 45% at 40% 12%, var(--sky-white) 0%, rgba(247,250,253,0) 70%),
      linear-gradient(150deg, var(--sky-white) 0%, var(--mist-blue) 38%, var(--mid-blue) 68%, var(--deep-blue) 86%, var(--navy) 100%);
  }
  .swoops {
    position: absolute;
    inset: 0;
  }
  .molecule-art {
    position: absolute;
    left: 0;
    top: 260px;
    width: 470px;
    height: 830px;
    background:
      radial-gradient(ellipse 55% 45% at 35% 55%, rgba(40,80,130,0.45) 0%, rgba(90,130,175,0.25) 45%, rgba(200,220,236,0) 75%),
      radial-gradient(circle at 60% 45%, rgba(224,120,80,0.28) 0%, rgba(224,120,80,0) 30%);
  }
  .cutout {
    position: absolute;
    top: 156px;
    width: 376px;
    height: 38px;
    background: var(--cutout);
    border: 1px solid var(--cutout-edge);
    box-sizing: border-box;
  }
  .cutout--left { left: 95px; }
  .cutout--right { left: 514px; }
  .title {
    position: absolute;
    top: 226px;
    left: 0;
    width: 985px;
    margin: 0;
    text-align: center;
    font-family: "Lexend Exa", sans-serif;
    font-weight: 700;
    font-size: 58px;
    line-height: 68px;
    letter-spacing: -3px;
    color: var(--title-blue);
  }
  .brand {
    position: absolute;
    left: 560px;
    top: 1094px;
    display: flex;
    align-items: center;
    gap: 16px;
    white-space: nowrap;
  }
  .brand-dot {
    width: 28px;
    height: 28px;
    border-radius: 50%;
    background: var(--mark-text);
  }
  .brand-name {
    font-family: "Lexend Exa", sans-serif;
    font-weight: 700;
    font-size: 34px;
    letter-spacing: -1px;
    color: var(--mark-text);
  }
</style>
</head>
<body>
  <main class="cover">
    <svg class="swoops" width="945" height="1200" viewBox="0 0 945 1200" aria-hidden="true">
      <path d="M0 560 C 250 470, 560 560, 945 420" fill="none" stroke="#ffffff" stroke-opacity="0.45" stroke-width="2"/>
      <path d="M0 600 C 300 520, 600 610, 945 470" fill="none" stroke="#ffffff" stroke-opacity="0.25" stroke-width="1.5"/>
      <path d="M120 1200 C 260 900, 600 640, 945 560 L 945 1200 Z" fill="#2a5f9c" fill-opacity="0.35"/>
      <path d="M260 1200 C 400 960, 650 760, 945 700 L 945 1200 Z" fill="#1b4a86" fill-opacity="0.45"/>
      <path d="M150 1200 C 300 880, 620 650, 945 590" fill="none" stroke="#ffffff" stroke-opacity="0.55" stroke-width="2"/>
      <path d="M600 0 C 700 300, 820 500, 945 560" fill="none" stroke="#ffffff" stroke-opacity="0.3" stroke-width="1.5"/>
    </svg>

    <div class="molecule-art" role="img" aria-label="Illustration of a glossy blue and orange molecular structure"></div>

    <div class="cutout cutout--left"></div>
    <div class="cutout cutout--right"></div>

    <h1 class="title">Hair Tissue<br>Mineral Analysis</h1>

    <div class="brand">
      <span class="brand-dot"></span>
      <span class="brand-name">Pevdosk</span>
    </div>
  </main>
</body>
</html>
```